Seeking funky, innovative business cards

I am looking to refresh our current business cards to something more engaging, visual and impactful. We are a management consultancy firm, see website (www.thornbury-partners.com.au). I've included our colour scheme, sample of the slides we use and our old business cards. We would like our cards to have icons. The card should display:- Name- Title- Mobile number- Address- Email address- Website - Company logo- Our purpose statement "We create the best places on earth to work"

Contact Information for Business Card

Radek Solvieri
Consultant
0491 627 358
Level 3, 218 Wexford Street, Melbourne 3000
radek@thornbury-partners.com.au
www.thornbury-partners.com.au

Purpose statement "we create the best places on earth to work"
LOGO available in google images

Font styles to use
Other font styles liked:
• Open Sans Light, Bebas Neue (open to other cool foints)

Colors
ffc214
5c5c5c
f5f5f5
fefefe

Requirements
Must have
• - Name
• - Title
• - Mobile number
• - Address
• - Email address
• - Website
• - Company logo
• - Our purpose statement "We create the best places on earth to work"
Nice to have
• - Icons
• - Colour (see our colour scheme"

```html
<!DOCTYPE html>
<html lang="en">
<head>
<meta charset="utf-8">
<title>Thornbury Partners – Business Card</title>
<link href="https://fonts.googleapis.com/css2?family=Lato:wght@300;400;700&display=swap" rel="stylesheet">
<style>
  :root {
    --backdrop: #1c1c1c;
    --card: #262626;
    --card-edge: #2e2e2e;
    --accent: #ffc214;
    --accent-deep: #f7a823;
    --ink: #f5f5f5;
    --ink-soft: #fefefe;
  }
  * { box-sizing: border-box; margin: 0; padding: 0; }
  html, body { width: 1200px; height: 900px; overflow: hidden; }
  body {
    background: var(--backdrop);
    font-family: "Lato", Arial, sans-serif;
    color: var(--ink);
    display: flex;
    flex-direction: column;
    align-items: center;
    justify-content: center;
    gap: 44px;
  }
  .card {
    position: relative;
    width: 720px;
    height: 380px;
    background: linear-gradient(135deg, var(--card) 0%, var(--card-edge) 70%, var(--card) 100%);
    border-bottom: 6px solid var(--accent-deep);
    box-shadow: 0 18px 40px rgba(0,0,0,.55);
  }
  .brand {
    display: flex;
    align-items: center;
    gap: 12px;
  }
  .brand-dot {
    width: 14px; height: 14px;
    border-radius: 50%;
    background: var(--accent);
    flex: none;
  }
  .brand-name {
    font-weight: 300;
    color: var(--ink-soft);
    line-height: 1;
    letter-spacing: -1px;
    white-space: nowrap;
  }

  .card-front {
    display: flex;
    flex-direction: column;
    align-items: center;
    justify-content: center;
    gap: 18px;
  }
  .card-front .brand-name { font-size: 62px; }
  .purpose {
    font-size: 15px;
    font-weight: 400;
    letter-spacing: 3px;
    text-transform: uppercase;
    color: var(--ink);
    padding-left: 26px;
  }

  .card-back { display: flex; align-items: center; }
  .card-back .brand { width: 350px; justify-content: center; padding-left: 16px; }
  .card-back .brand-name { font-size: 34px; }
  .divider {
    width: 2px; height: 220px;
    background: var(--accent);
    margin: 0 22px 0 6px;
    flex: none;
  }
  .details { flex: 1; }
  .person-name {
    font-weight: 700;
    font-size: 26px;
    letter-spacing: 2.5px;
    text-transform: uppercase;
    color: var(--accent);
    line-height: 1.05;
  }
  .person-title { font-size: 16px; margin-top: 4px; }
  .address { font-size: 16px; line-height: 1.35; margin-top: 16px; }
  .contact-list { list-style: none; margin-top: 14px; }
  .contact-list li {
    display: flex; align-items: center; gap: 12px;
    font-size: 16px; line-height: 1.7;
    white-space: nowrap;
  }
  .contact-list svg { width: 14px; height: 14px; flex: none; }
</style>
</head>
<body>
  <section class="card card-front">
    <div class="brand">
      <span class="brand-dot"></span>
      <span class="brand-name">Thornbury Partners</span>
    </div>
    <p class="purpose">We create the best places on earth to work</p>
  </section>

  <section class="card card-back">
    <div class="brand">
      <span class="brand-dot"></span>
      <span class="brand-name">Thornbury Partners</span>
    </div>
    <div class="divider"></div>
    <div class="details">
      <h1 class="person-name">Radek Solvieri</h1>
      <p class="person-title">Consultant</p>
      <p class="address">Level 3, 218 Wexford Street<br>Melbourne, VIC 3000</p>
      <ul class="contact-list">
        <li>
          <svg viewBox="0 0 16 16" aria-hidden="true"><path d="M4 1l2.5 3-1.5 1.5c.8 2 2.5 3.7 4.5 4.5L11 8.5 14 11l-1.5 3C7 14 2 9 2 3.5z" fill="none" stroke="#ffc214" stroke-width="1.4" stroke-linejoin="round"/></svg>
          0491 627 358
        </li>
        <li>
          <svg viewBox="0 0 16 16" aria-hidden="true"><rect x="4" y="2" width="8" height="4" fill="#ffc214"/><rect x="1" y="6" width="14" height="6" rx="1" fill="#ffc214"/><rect x="4" y="10" width="8" height="4" fill="#262626" stroke="#ffc214"/></svg>
          +61 3 9340 2716
        </li>
        <li>
          <svg viewBox="0 0 16 16" aria-hidden="true"><rect x="1.5" y="3.5" width="13" height="9" fill="none" stroke="#ffc214" stroke-width="1.3"/><path d="M1.5 3.5L8 9l6.5-5.5" fill="none" stroke="#ffc214" stroke-width="1.3"/></svg>
          radek@thornbury-partners.com.au
        </li>
        <li>
          <svg viewBox="0 0 16 16" aria-hidden="true"><circle cx="8" cy="8" r="6.3" fill="none" stroke="#ffc214" stroke-width="1.2"/><ellipse cx="8" cy="8" rx="2.8" ry="6.3" fill="none" stroke="#ffc214" stroke-width="1.1"/><path d="M1.7 8h12.6M3 4.5h10M3 11.5h10" stroke="#ffc214" stroke-width="1"/></svg>
          www.thornbury-partners.com.au
        </li>
      </ul>
    </div>
  </section>
</body>
</html>
```